Velmora Partners - website for real estate investment company

Create a bold, modern website that reflects Velmora’s success, professionalism, and credibility.
The design must stand out while maintaining a polished, corporate tone. (bold, but understated)
The client just created a new logo, and the website design must be in sync with the logo design. Information about the logo colors, fonts, and message are in the attached design brief.
Updates

Target Market(s)

b2b: banks, brokers, institutional partners, vendors, and property sellers.

Industry/Entity Type

real estate investment company

Number of Pages Required

1 page

Font styles to use
Sans Serif

Colors

Designer to choose colors to be used in the design.

Requirements
Must have
• 1. homepage design (psd) 2. a top banner image (psd) for a default inner page
Nice to have
• please see attached design brief
Should not have

```html
<!DOCTYPE html>
<html lang="en">
<head>
<meta charset="utf-8">
<title>Velmora Partners</title>
<link href="https://fonts.googleapis.com/css2?family=Poppins:wght@400;500;600;700&display=swap" rel="stylesheet">
<style>
:root{
  --red:#e31e24;
  --ink:#1d1d1d;
  --body:#555;
  --muted:#777;
  --logo:#3b3b3b;
  --card:#f7f7f7;
  --card-hi:#fdeeee;
  --faint:#f1f1f1;
  --line:#e6e6e6;
  --dark:#1f252b;
}
*{box-sizing:border-box;margin:0;padding:0}
html,body{width:1200px;height:3550px;overflow:hidden;background:#fff}
body{position:relative;font-family:'Poppins',sans-serif;color:var(--ink)}
.abs{position:absolute}
.nav a{position:absolute;top:32px;font-size:14px;color:var(--ink);text-decoration:none}
.logo{font-family:'Poppins',sans-serif;font-weight:700;color:var(--logo);letter-spacing:1px}
.btn{position:absolute;background:var(--red);color:#fff;font-weight:600;font-size:15px;display:flex;align-items:center;justify-content:center}
.center{left:0;width:1200px;text-align:center}
.h2{font-weight:600;font-size:29px;letter-spacing:.5px}
.p{font-size:13.5px;line-height:21px;color:var(--body)}
.stat{position:absolute;text-align:center;width:220px}
.stat b{display:block;font-size:27px;font-weight:600;color:#333}
.stat span{display:block;font-size:10.5px;font-weight:600;line-height:16px;margin-top:6px}
.vline{position:absolute;width:1px;background:var(--line)}
.card{position:absolute;top:1298px;width:259px;height:259px;background:var(--card)}
.card.hi{background:var(--card-hi)}
.card .ico{position:absolute;left:26px;top:26px;width:70px;height:70px;background:#4a4a4a;display:flex;align-items:center;justify-content:center}
.card.hi .ico{background:var(--red)}
.card h3{position:absolute;left:26px;top:152px;font-size:17px;font-weight:600;line-height:23px;color:#444}
.card.hi h3{color:var(--ink)}
.card p{position:absolute;left:26px;top:195px;width:200px;font-size:13px;line-height:20px;color:var(--muted)}
.photo{position:absolute}
.num{position:absolute;font-size:118px;font-weight:700;color:var(--faint);line-height:1}
.feat h4{font-size:17px;font-weight:600;color:#333}
.feat p{font-size:13px;line-height:20px;color:var(--muted);margin-top:10px}
.redbox{position:absolute;width:60px;height:60px;background:var(--red);display:flex;align-items:center;justify-content:center}
.contact-bg{position:absolute;left:0;top:2716px;width:1200px;height:540px;background:linear-gradient(180deg,#2a3036 0%,#1e2328 60%,#262c30 100%)}
.cbox{position:absolute;width:46px;height:46px;border:2px solid #fff;background:#fff;display:flex;align-items:center;justify-content:center;box-shadow:0 0 0 3px rgba(255,255,255,.25)}
.clabel{position:absolute;font-size:13px;color:#ddd}
.cval{position:absolute;font-size:16px;font-weight:600;color:#fff}
.field{position:absolute;height:41px;border:1px solid rgba(255,255,255,.25);background:rgba(255,255,255,.12);font-size:13px;color:#eee;padding:12px 18px}
.field.light{background:#fff;color:var(--ink)}
.flabel{position:absolute;font-size:13px;color:#333}
.fval{position:absolute;font-size:16px;font-weight:600;color:var(--ink);line-height:21px}
.links{position:absolute;top:3462px;left:0;width:1200px;text-align:center;font-size:13px;color:#555;word-spacing:2px}
.links i{font-style:normal;margin:0 14px;color:#777}
</style>
</head>
<body>

<!-- Navigation -->
<nav class="nav">
  <a style="left:61px">Home</a>
  <a style="left:133px">Our Story</a>
  <a style="left:227px">Investment Strategy</a>
  <a style="left:808px">What Sets Us Apart</a>
  <a style="left:972px">Our Portfolio</a>
  <a style="left:1085px">Contact</a>
</nav>
<div class="abs logo center" style="top:12px;font-size:42px">VELMORA</div>

<!-- Hero -->
<div class="photo" role="img" aria-label="Upward view of glass skyscrapers against a pale sky" style="left:0;top:352px;width:1200px;height:321px;background:linear-gradient(180deg,#ffffff 0%,#c9cfd6 18%,#6f7b88 45%,#2e3845 75%,#151b23 100%)"></div>
<h1 class="abs center" style="top:168px;font-size:49px;font-weight:700;line-height:59px;letter-spacing:.5px">EXPERIENCE.<br>STRATEGY. VISION</h1>
<p class="abs center" style="top:301px;font-size:15.5px;line-height:24px;color:#444">Velmora Partners is a vertically integrated real estate investment firm with a<br>proven four-decade track record.</p>
<div class="btn" style="left:525px;top:372px;width:150px;height:41px">Contact Us</div>

<!-- Our Story -->
<h2 class="abs center h2" style="top:746px">OUR STORY</h2>
<p class="abs p" style="left:280px;top:798px;width:640px;text-align:center">Velmora Partners is a vertically integrated real estate investment firm with a proven four-decade track record. We acquire, reposition, and operate high-performing assets across multiple sectors — always with a focus on exceptional, risk-adjusted returns.</p>
<p class="abs p" style="left:280px;top:871px;width:640px;text-align:center">Velmora Partners is a vertically integrated real estate investment firm with a proven<br>four-decade track record.</p>
<div class="stat" style="left:270px;top:944px"><b>1989</b><span>FOUNDED</span></div>
<div class="vline" style="left:478px;top:937px;height:75px"></div>
<div class="stat" style="left:483px;top:934px"><b>23,000+</b><span>MULTIFAMILY &amp;<br>HEALTHCARE UNITS</span></div>
<div class="vline" style="left:706px;top:937px;height:75px"></div>
<div class="stat" style="left:729px;top:944px"><b>$300M+</b><span>INVESTED IN ENOVATIONS</span></div>
<div class="btn" style="left:525px;top:1034px;width:150px;height:41px">View Story</div>
<div class="abs" style="left:0;top:1150px;width:1200px;height:1px;background:var(--faint)"></div>

<!-- Investment Strategy -->
<h2 class="abs center h2" style="top:1222px">INVESTMENT STRATEGY</h2>
<div class="card" style="left:60px">
  <div class="ico"><svg width="44" height="44" viewBox="0 0 44 44" fill="none" stroke="#fff" stroke-width="2"><rect x="4" y="4" width="10" height="9"/><rect x="17" y="4" width="10" height="9"/><rect x="30" y="4" width="10" height="9"/><path d="M9 13v6h26v-6M22 13v10"/><path d="M4 34l8-6h10l6 3h-9M4 40h20l16-9-4-3-10 5"/></svg></div>
  <h3>Disciplined<br>Acquisition</h3><p>Lorem Ipsum has been the industry's standard.</p>
</div>
<div class="card hi" style="left:333px">
  <div class="ico"><svg width="44" height="44" viewBox="0 0 44 44" fill="none" stroke="#fff" stroke-width="2"><circle cx="22" cy="22" r="16"/><path d="M12 24l10-9 10 9M15 22v9h14v-9"/><rect x="20" y="25" width="4" height="6"/><path d="M36 12l2-5M8 32l-2 5"/></svg></div>
  <h3>Value-Add<br>Renovations</h3><p>Lorem Ipsum has been the industry's standard.</p>
</div>
<div class="card" style="left:608px">
  <div class="ico"><svg width="44" height="44" viewBox="0 0 44 44" fill="none" stroke="#fff" stroke-width="2"><rect x="5" y="6" width="34" height="24"/><path d="M18 30l-2 7h12l-2-7M13 37h18"/><circle cx="18" cy="18" r="5"/><path d="M26 14h8M26 19h8M26 24h6"/></svg></div>
  <h3>Long- term<br>Operations</h3><p>Lorem Ipsum has been the industry's standard.</p>
</div>
<div class="card" style="left:881px">
  <div class="ico"><svg width="44" height="44" viewBox="0 0 44 44" fill="none" stroke="#fff" stroke-width="2"><path d="M8 26a15 15 0 0 1 22-17M36 18a15 15 0 0 1-22 17"/><circle cx="33" cy="10" r="5"/><circle cx="11" cy="34" r="5"/><path d="M17 28v-4M22 28v-8M27 28v-11"/></svg></div>
  <h3>Risk-Adjusted<br>Returns</h3><p>Lorem Ipsum has been the industry's standard.</p>
</div>

<!-- Portfolio -->
<div class="photo" role="img" aria-label="City skyline with twin towers above a green park at sunrise" style="left:114px;top:1694px;width:317px;height:316px;background:linear-gradient(180deg,#6fa3d6 0%,#b7cde0 40%,#b39a86 65%,#3d5a3a 100%)"></div>
<div class="photo" role="img" aria-label="Looking up between tall glass towers into a bright sky" style="left:442px;top:1632px;width:144px;height:344px;background:linear-gradient(90deg,#8b98a6 0%,#eef1f4 45%,#f7f8fa 60%,#9aa6b2 100%)"></div>
<h2 class="abs" style="left:643px;top:1686px;font-size:30px;font-weight:600;line-height:39px;letter-spacing:.3px">OUR REAL- ESTATE Portfolio<br>AT YOUR FINGERTIPS</h2>
<p class="abs p" style="left:643px;top:1777px;width:440px;font-size:13px">Lorem Ipsum has been the industry's standard dummy text ever since the 1500s, when an unknown printer took a galley of type and scrambled it to make a type specimen book. It has survived not only five centuries, but also the leap into electronic typesetting, remaining essentially unchanged.</p>
<div class="btn" style="left:641px;top:1910px;width:150px;height:40px">View Story</div>

<!-- What Sets Us Apart -->
<h2 class="abs center h2" style="top:2082px">WHAT SEATS US APART</h2>
<div class="num" style="left:333px;top:2178px">01</div>
<div class="num" style="left:756px;top:2178px">02</div>
<div class="num" style="left:620px;top:2474px">03</div>
<svg class="abs" style="left:444px;top:2152px" width="312" height="312" viewBox="0 0 312 312"><circle cx="156" cy="156" r="153" fill="none" stroke="#555" stroke-width="2"/></svg>
<div class="photo" role="img" aria-label="Night city skyline seen from above" style="left:452px;top:2160px;width:296px;height:296px;border-radius:50%;background:radial-gradient(circle at 50% 40%,#5a6b7c 0%,#34404c 50%,#1d242c 100%)"></div>
<div class="abs logo" style="left:452px;top:2271px;width:296px;text-align:center;font-size:50px;color:#a8c4de">VELMORA</div>

<div class="abs feat" style="left:60px;top:2239px;width:253px;text-align:right"><h4>Discover properties</h4><p>Lorem Ipsum has been the industry's standard dummy text ever since the 1500s</p></div>
<div class="redbox" style="left:345px;top:2240px"><svg width="34" height="34" viewBox="0 0 34 34" fill="none" stroke="#fff" stroke-width="2"><circle cx="19" cy="14" r="9"/><path d="M12 21l-8 8"/><path d="M15 15l4-4 4 4v4h-8z"/></svg></div>
<div class="redbox" style="left:788px;top:2240px"><svg width="34" height="34" viewBox="0 0 34 34" fill="none" stroke="#fff" stroke-width="2"><path d="M12 30V20M18 30V14M24 30V8M30 30V4"/><circle cx="7" cy="25" r="5"/><path d="M6 14l10-8M12 6h4v4"/></svg></div>
<div class="abs feat" style="left:872px;top:2239px;width:240px"><h4>Invest With Confidence</h4><p>Lorem Ipsum has been the industry's standard dummy text ever since the 1500s</p></div>
<div class="redbox" style="left:569px;top:2497px"><svg width="34" height="34" viewBox="0 0 34 34" fill="none" stroke="#fff" stroke-width="2"><circle cx="22" cy="14" r="7"/><path d="M22 10v8M20 12h4M4 24l6-4h8l4 3h-6M4 30h14l12-8-3-2-8 4"/><path d="M8 6h6v6"/></svg></div>
<div class="abs feat center" style="top:2576px"><h4>Earn &amp; track</h4><p>Lorem Ipsum has been the industry's<br>standard dummy.</p></div>

<!-- Contact -->
<div class="contact-bg" role="img" aria-label="Dimmed city skyline with twin towers"></div>
<h2 class="abs center h2" style="top:2787px;color:#fff">CONTACT US</h2>
<div class="cbox" style="left:379px;top:2868px"><svg width="22" height="22" viewBox="0 0 24 24" fill="var(--red)"><path d="M6.6 10.8a15 15 0 0 0 6.6 6.6l2.2-2.2a1 1 0 0 1 1-.25 11.4 11.4 0 0 0 3.6.57 1 1 0 0 1 1 1V20a1 1 0 0 1-1 1A17 17 0 0 1 3 4a1 1 0 0 1 1-1h3.5a1 1 0 0 1 1 1c0 1.25.2 2.45.57 3.57a1 1 0 0 1-.25 1z"/></svg></div>
<div class="clabel" style="left:445px;top:2871px">Call Now</div>
<div class="cval" style="left:445px;top:2892px">+ (555) 014-2876</div>
<div class="cbox" style="left:628px;top:2868px"><svg width="22" height="22" viewBox="0 0 24 24" fill="var(--red)"><path d="M3 6h18v12H3z"/><path d="M3 6l9 7 9-7" stroke="#fff" stroke-width="1.6" fill="none"/></svg></div>
<div class="clabel" style="left:700px;top:2871px">Email</div>
<div class="cval" style="left:700px;top:2892px">info@velmora.com</div>
<div class="field light" style="left:194px;top:2963px;width:263px">Name *</div>
<div class="field" style="left:468px;top:2963px;width:264px">Phone *</div>
<div class="field" style="left:741px;top:2963px;width:264px">Email *</div>
<div class="field" style="left:194px;top:3019px;width:811px;height:91px">Message *</div>
<div class="btn" style="left:530px;top:3140px;width:137px;height:40px;font-size:14px">SUBMIT</div>

<!-- Footer -->
<div class="abs logo center" style="top:3298px;font-size:42px">VELMORA</div>
<svg class="abs" style="left:405px;top:3380px" width="20" height="20" viewBox="0 0 24 24" fill="var(--red)"><path d="M6.6 10.8a15 15 0 0 0 6.6 6.6l2.2-2.2a1 1 0 0 1 1-.25 11.4 11.4 0 0 0 3.6.57 1 1 0 0 1 1 1V20a1 1 0 0 1-1 1A17 17 0 0 1 3 4a1 1 0 0 1 1-1h3.5a1 1 0 0 1 1 1c0 1.25.2 2.45.57 3.57a1 1 0 0 1-.25 1z"/></svg>
<div class="flabel" style="left:443px;top:3380px">Call Now</div>
<div class="fval" style="left:443px;top:3402px">+ (555) 014-2876</div>
<div class="vline" style="left:608px;top:3378px;height:50px"></div>
<svg class="abs" style="left:638px;top:3382px" width="20" height="22" viewBox="0 0 24 26" fill="var(--red)"><path d="M12 1a8 8 0 0 0-8 8c0 6 8 13 8 13s8-7 8-13a8 8 0 0 0-8-8zm0 11a3 3 0 1 1 0-6 3 3 0 0 1 0 6z"/></svg>
<div class="flabel" style="left:675px;top:3382px">Location</div>
<div class="fval" style="left:675px;top:3403px">240 Harbor Rd.,<br>Linden Bay, NJ 07012</div>
<div class="links">Home<i>|</i>Our Story<i>|</i>Investment Strategy<i>|</i>What Sets Us Apart<i>|</i>Our Portfolio<i>|</i>Contact</div>
<div class="abs" style="left:0;top:3500px;width:1200px;height:1px;background:var(--line)"></div>
<div class="abs center" style="top:3517px;font-size:13px;color:#333">Copyright ©2025 velmora.All rights reserved</div>

</body>
</html>
```